New digital business consulting firm needs a professional Wordpress site

Lanternby Works Inc. is a new consulting firm that helps large companies with Digital Transformation. We help companies define a digital transformation strategy for improving the products, processes and customer journey using digital technology.

The website will serve three purposes:
1) Represent what the firm does.
2) Allow people to download research reports.
3) Collect email addresses from people who my be interested in using our services.

The tone of the website should be innovative and professional. The website will have only a few pages. You can see the type of content we wish to post on the current website www.lanternbyworks.example.

The website will support a book that is about to be released. The book cover is attached. However, the website does not necessarily have to match the book cover. Do not be constrained by the book cover.

Target Market(s)

Executives in large companies

Industry/Entity Type

Management Consulting

Font styles to use
Sans Serif

Requirements
Must have
• Professional and innovative, clean, cool
Nice to have
• None
Should not have
• None

```html
<!DOCTYPE html>
<html lang="en">
<head>
<meta charset="utf-8">
<title>Lanternby Works — Digital Transformation Strategy</title>
<link rel="stylesheet" href="https://fonts.googleapis.com/css2?family=Open+Sans:wght@400;600;700;800&display=swap">
<style>
:root{
  --navy:#0b1a4a;
  --brand:#1d4f86;
  --heading:#1e4a78;
  --text:#2a2a2a;
  --muted:#7a7a7a;
  --pale:#eef3fa;
  --yellow:#f5d90a;
  --hero-a:#2a6fcf;
  --hero-b:#5c9ae6;
  --band:#0b4f98;
  --footer:#2b2b2b;
  --accent-green:#5a8f2e;
}
*{box-sizing:border-box;margin:0;padding:0}
html,body{width:1200px;height:2406px;overflow:hidden}
body{font-family:"Open Sans",Arial,sans-serif;color:var(--text);background:#fff;position:relative}
.section{position:absolute;left:0;width:1200px}
.header{top:0;height:100px;background:#fff}
.logo{position:absolute;left:132px;top:30px;font-size:37px;font-weight:600;color:var(--brand);letter-spacing:-0.5px}
.nav{position:absolute;right:133px;top:44px;display:flex;gap:40px;font-size:13px;color:#555}
.nav .active{color:var(--brand);position:relative}
.nav .active::before{content:"";position:absolute;left:-11px;top:6px;width:5px;height:5px;border-radius:50%;background:var(--accent-green)}
.hero{top:100px;height:513px}
.hero-photo{position:absolute;inset:0;background:linear-gradient(120deg,var(--hero-a) 0%,var(--hero-b) 45%,#3f7fd6 70%,#2464c0 100%)}
.hero-title{position:absolute;top:276px;width:100%;text-align:center;color:#fff;font-size:42px;font-weight:800;letter-spacing:0.5px}
.hero-sub{position:absolute;top:328px;width:100%;text-align:center;color:#fff;font-size:21px;font-weight:600}
.play{position:absolute;left:571px;top:367px}
.services{top:613px;height:329px;background:var(--pale)}
.service{position:absolute;top:78px;width:300px;text-align:center}
.service svg{display:block;margin:0 auto}
.service h3{font-size:21px;font-weight:400;color:var(--heading);margin-top:14px}
.service p{font-size:11px;color:var(--muted);line-height:16px;margin:12px auto 0;width:280px}
.btn-more{display:inline-block;margin-top:16px;background:#fff;width:96px;height:34px;line-height:34px;font-size:11px;color:var(--accent-green);text-decoration:underline}
.book{top:942px;height:559px;background:#fff}
.cover{position:absolute;left:132px;top:80px;width:264px;height:399px;background:linear-gradient(180deg,#0b1648 0%,#0a1442 80%,#1a2a4a 100%)}
.book h2,.research h2{font-size:42px;font-weight:400;color:var(--heading)}
.book h2{position:absolute;left:457px;top:106px}
.book .lead{position:absolute;left:459px;top:172px;width:608px;font-size:16px;line-height:27px}
.book .body{position:absolute;left:459px;top:273px;width:608px;font-size:11.5px;line-height:21px;color:var(--muted)}
.btn-cta{position:absolute;background:var(--navy);color:var(--yellow);font-weight:700;font-size:24px;text-align:center}
.book .btn-cta{left:459px;top:376px;width:192px;height:65px;line-height:65px}
.research{top:1501px;height:342px;background:var(--pale)}
.research h2{position:absolute;left:130px;top:46px}
.research p{position:absolute;left:132px;top:112px;width:530px;font-size:17.5px;line-height:28px}
.research .btn-cta{left:132px;top:217px;width:256px;height:62px;line-height:62px}
.laptop{position:absolute;left:682px;top:52px;width:425px;height:231px;background:linear-gradient(180deg,#2b3e55 0%,#1e2e44 85%,#cfd2d6 88%,#9a9ea4 100%);border-radius:10px 10px 4px 4px}
.testimonials{top:1843px;height:363px;background:#fff;text-align:center}
.testimonials h3{position:absolute;top:82px;width:100%;font-size:21px;font-weight:400;color:var(--heading)}
.quote{position:absolute;left:132px;top:122px;width:935px;font-size:16px;line-height:25px;color:#666}
.quote .mark{color:#999;font-weight:800;font-size:22px;vertical-align:-3px}
.cite{position:absolute;top:186px;width:100%;font-size:13px;color:#333}
.avatar{position:absolute;left:571px;top:220px;width:58px;height:58px;border-radius:50%;background:linear-gradient(180deg,#d9dde2,#b7bec7);border:3px solid #fff;box-shadow:0 0 0 1px #ddd}
.arrow{position:absolute;top:134px}
.newsletter{top:2206px;height:96px;background:var(--band)}
.nl-label{position:absolute;left:263px;top:32px;color:#fff;font-size:24px;font-weight:400;display:flex;align-items:center;gap:10px}
.nl-input{position:absolute;left:600px;top:28px;width:239px;height:39px;background:#fff;font-size:10px;color:#999;padding:13px 16px}
.nl-btn{position:absolute;left:839px;top:28px;width:96px;height:39px;background:#1c1c1c;color:#fff;font-size:11px;font-weight:600;text-align:center;line-height:39px}
.footer{top:2302px;height:104px;background:var(--footer)}
.foot-links{position:absolute;left:132px;top:30px;font-size:10px;color:#bbb}
.foot-links span{margin:0 8px;color:#777}
.copy{position:absolute;left:132px;top:57px;font-size:10px;color:#999}
.social{position:absolute;left:976px;top:39px;display:flex;gap:8px}
.social i{display:block;width:24px;height:24px;border-radius:50%;background:#2f6fc0}
</style>
</head>
<body>

<header class="section header">
  <div class="logo">Lanternby Works</div>
  <nav class="nav">
    <span class="active">Home</span><span>Book</span><span>Services</span><span>Downloadable Research</span><span>Contact Us</span>
  </nav>
</header>

<section class="section hero">
  <div class="hero-photo" role="img" aria-label="Blue-toned photo of hands using a phone and a laptop keyboard with floating device icons"></div>
  <h1 class="hero-title">DIGITAL TRANSFORMATION STRATEGY</h1>
  <p class="hero-sub">For Improving The Products, Processes And Customer Journey Using Digital Technology.</p>
  <svg class="play" width="58" height="58" viewBox="0 0 58 58" aria-label="Play video"><circle cx="29" cy="29" r="29" fill="#fff"/><path d="M23 18 L41 29 L23 40 Z" fill="var(--brand)"/></svg>
</section>

<section class="section services">
  <div class="service" style="left:126px">
    <svg width="36" height="34" viewBox="0 0 36 34" fill="none" stroke="var(--heading)" stroke-width="3"><path d="M5 24 V17 a13 13 0 0 1 26 0 V24"/><rect x="3" y="19" width="7" height="12" rx="2" fill="var(--heading)"/><rect x="26" y="19" width="7" height="12" rx="2" fill="var(--heading)"/></svg>
    <h3>Speaking Engagements</h3>
    <p>Provide an overview of the state of digital technology and implications for products, processes and customer journey.</p>
    <span class="btn-more">READ MORE</span>
  </div>
  <div class="service" style="left:450px">
    <svg width="40" height="34" viewBox="0 0 40 34" fill="none" stroke="var(--heading)" stroke-width="3"><rect x="3" y="6" width="26" height="25" rx="3"/><path d="M16 22 L19 14 L34 2 L38 6 L23 18 Z" fill="#fff"/></svg>
    <h3>Digital Assessment</h3>
    <p>Help your company assess the state of your digital transformation.</p>
    <span class="btn-more">READ MORE</span>
  </div>
  <div class="service" style="left:774px">
    <svg width="26" height="36" viewBox="0 0 26 36" fill="none" stroke="var(--heading)" stroke-width="3"><path d="M8 24 C8 18 3 16 3 11 a10 10 0 0 1 20 0 C23 16 18 18 18 24 Z"/><path d="M8 29 H18 M10 34 H16"/></svg>
    <h3>Digital Strategy Development</h3>
    <p>Based on the digital assessment and your objective, help define a digital vision and a strategy for implementation.</p>
    <span class="btn-more">READ MORE</span>
  </div>
</section>

<section class="section book">
  <div class="cover" role="img" aria-label="Cover of the book Making Digital Work by Marcel Dufresne, navy with yellow title lettering"></div>
  <h2>Book</h2>
  <p class="lead">Making Digital Work is a manual for winning in the next digital era. Its author, Marcel Dufresne, has been helping large companies establish and execute digital strategies for 25 years.</p>
  <p class="body">It is critical for any executive in any function to understand key digital technologies, the way they are evolving, how companies can leverage them to improve products, processes, and the customer journey, and what kind of business outcomes can be derived. All of that, moreover, is useless without knowing how to help your company define its digital vision and how to act on it. This book covers those topics to help you thrive in the new digital era.</p>
  <div class="btn-cta">ORDER NOW</div>
</section>

<section class="section research">
  <h2>Downloadable Research</h2>
  <p>Duis eget porttitor ante. Proin varius consectetur augue nec aliquam. Vivamus tempor a neque non lacinia. Mauris feugiat felis quis ultrices porttitor inceptos himenaeos.</p>
  <div class="btn-cta">DOWNLOAD NOW</div>
  <div class="laptop" role="img" aria-label="Laptop showing research worksheet pages"></div>
</section>

<section class="section testimonials">
  <svg class="arrow" style="left:22px" width="20" height="32" viewBox="0 0 20 32" fill="none" stroke="#ccc" stroke-width="3"><path d="M16 2 L4 16 L16 30"/></svg>
  <svg class="arrow" style="left:1158px" width="20" height="32" viewBox="0 0 20 32" fill="none" stroke="#ccc" stroke-width="3"><path d="M4 2 L16 16 L4 30"/></svg>
  <h3>Testimonials</h3>
  <p class="quote"><span class="mark">&ldquo;</span> Curabitur congue, metus euismod dapibus congue, velit ligula pellentesque lorem, vel dignissim quam erat pulvinar tortor. Suspendisse potenti. Donec eget leo sed libero pulvinar dapibus ac vel eros. <span class="mark">&rdquo;</span></p>
  <p class="cite">~ Peter Hale, Company name</p>
  <div class="avatar" role="img" aria-label="Portrait of the client giving the testimonial"></div>
</section>

<section class="section newsletter">
  <div class="nl-label">
    <svg width="22" height="18" viewBox="0 0 22 18" fill="none" stroke="#fff" stroke-width="2"><rect x="1" y="1" width="20" height="16" rx="2"/><path d="M1 3 L11 10 L21 3"/></svg>
    NEWSLETTER SUBSCRIBE
  </div>
  <div class="nl-input">Email Address</div>
  <div class="nl-btn">SUBSCRIBE</div>
</section>

<footer class="section footer">
  <div class="foot-links">Home<span>|</span>Book<span>|</span>Services<span>|</span>Downloadable Research<span>|</span>Contact Us</div>
  <div class="copy">Copyright © 2017 Company name. All rights reserved.</div>
  <div class="social"><i aria-label="Social link"></i><i aria-label="Social link"></i><i aria-label="Social link"></i></div>
</footer>

</body>
</html>
```